Rollup Banner & Flyer für eine Messe "Erfolg durch Innovation"

Wir benötigten für eine Messe einen Roll Up Banner und Flyer zum verteilen. Gerne basierend auf der aktuellen Firmenpräsentation und mit unseren Referenzen.
Im flyer sollen unserer Leistungen (Datenanalyse, Simulation, Optimierung und Webapplikation) dargestellt werden mit einem kleinen Text und einem aussagekräftigen bild. (https://www.kalvento.ch/leistungen/)

Target Market(s)

Industrie

Industry/Entity Type

Simulation

Font styles to use
Sans Serif
Other font styles liked:
• Roboto

Requirements
Must have
• Logo, Referenzen

```html
<!DOCTYPE html>
<html lang="de">
<head>
<meta charset="utf-8">
<title>Kalvento – Erfolg durch Innovation</title>
<link href="https://fonts.googleapis.com/css2?family=Roboto:wght@400;500;700;900&display=swap" rel="stylesheet">
<style>
  :root{
    --navy:#1c2347;
    --navy-deep:#141a38;
    --lime:#dbe25b;
    --lime-soft:#e6ea7d;
    --white:#ffffff;
    --sky:#6f9fdc;
    --stage:#eceae4;
  }
  *{margin:0;padding:0;box-sizing:border-box}
  html,body{width:800px;height:1200px;overflow:hidden;background:var(--stage)}
  body{font-family:"Roboto",Arial,sans-serif;position:relative}
  .banner{position:absolute;left:165px;top:12px;width:470px;height:1176px;overflow:hidden;background:var(--navy)}
  .banner > *{position:absolute}
  .hero-photo{left:0;top:0;width:470px;height:345px;background:linear-gradient(160deg,#c9d6e6 0%,#8fb1dd 45%,#4f86d2 100%)}
  .person-photo{left:215px;top:30px;width:255px;height:315px;border-radius:120px 0 0 0;background:linear-gradient(180deg,#3c4660 0%,#2f3853 60%,#5a6787 100%);opacity:.9}
  .shapes{left:0;top:0;width:470px;height:1176px}
  .logo-tab{left:27px;top:0;width:88px;height:103px;background:var(--white);border-radius:0 0 44px 44px;display:flex;flex-direction:column;align-items:center;justify-content:center;gap:6px}
  .logo-tab .dot{width:34px;height:34px;border-radius:50%;background:var(--navy)}
  .logo-tab .name{font-size:12px;font-weight:700;color:var(--navy)}
  .headline{left:27px;top:204px;color:var(--white);font-weight:900;line-height:.98;text-transform:uppercase}
  .headline .l1{font-size:40px;display:block}
  .headline .l2{font-size:50px;display:block}
  .headline .l3{font-size:29px;display:block;letter-spacing:.3px}
  .brand{left:0;top:380px;width:470px;text-align:center}
  .brand .name{font-size:26px;font-weight:700;color:var(--lime);display:inline-flex;align-items:center;gap:8px;letter-spacing:.5px}
  .brand .name::before{content:"";width:22px;height:22px;border-radius:50%;background:var(--lime)}
  .brand .tag{display:block;font-size:8px;font-weight:700;color:var(--lime);letter-spacing:1px;margin-top:1px;padding-left:30px}
  .pill{border-radius:20px;font-weight:700;text-transform:uppercase;display:flex;align-items:center;justify-content:center}
  .pill-about{left:138px;top:442px;width:204px;height:36px;background:var(--lime);color:var(--navy);font-size:15px}
  .service-photo{width:78px;height:78px;border-radius:50%;border:5px solid var(--white);box-shadow:0 0 0 5px var(--lime)}
  .ph1{left:31px;top:519px;background:linear-gradient(135deg,#9fb6cf,#4d6079)}
  .ph2{left:142px;top:519px;background:linear-gradient(135deg,#7ea0c7,#2c3d5e)}
  .ph3{left:252px;top:519px;background:linear-gradient(135deg,#4a4f5e,#c07b4e)}
  .ph4{left:363px;top:519px;background:linear-gradient(135deg,#f1b233,#7a5620)}
  .service-label{top:623px;height:19px;background:var(--lime);color:var(--navy);font-size:10px;font-weight:700;border-radius:10px;display:flex;align-items:center;justify-content:center}
  .lb1{left:28px;width:82px}.lb2{left:142px;width:78px}.lb3{left:250px;width:82px}.lb4{left:360px;width:84px}
  .service-text{top:661px;width:78px;font-size:6.9px;line-height:1.55;color:var(--white);text-align:center}
  .tx1{left:31px}.tx2{left:142px}.tx3{left:252px}.tx4{left:363px}
  .pill-grow{left:118px;top:849px;width:228px;height:37px;background:var(--navy);color:var(--white);font-size:16px}
  .grow-copy{left:113px;top:898px;width:244px;text-align:center;font-size:12.4px;line-height:1.35;color:var(--navy)}
  .call{left:124px;top:996px;display:flex;align-items:center;gap:10px;color:var(--navy)}
  .call .label{font-size:15px;display:block;line-height:1}
  .call .number{font-size:25px;font-weight:700;display:block;line-height:1.1}
  .footer-info{left:0;top:1110px;width:470px;height:44px;display:flex;justify-content:center;color:var(--white)}
  .info-item{display:flex;align-items:center;gap:7px;padding:0 13px;font-size:7.6px;line-height:1.4;font-weight:500;text-transform:uppercase}
  .info-item + .info-item{border-left:1px dashed rgba(255,255,255,.5)}
  .info-item .icon{width:18px;height:18px;flex:none}
  .info-item .small{font-size:6px;display:block}
  .info-item .mail{font-size:11px;text-transform:none;display:block}
</style>
</head>
<body>
<main class="banner">
  <div class="hero-photo" role="img" aria-label="Photo of a modern glass office building with bare tree branches against a blue sky"></div>
  <div class="person-photo" role="img" aria-label="Photo of a businessman in a grey suit giving an OK hand sign"></div>

  <svg class="shapes" viewBox="0 0 470 1176" aria-hidden="true">
    <defs>
      <linearGradient id="limeFade" x1="0" x2="1" y1="0" y2="0">
        <stop offset="0" stop-color="#dbe25b"/>
        <stop offset="1" stop-color="#dbe25b" stop-opacity=".15"/>
      </linearGradient>
    </defs>
    <circle cx="360" cy="70" r="78" fill="none" stroke="#dbe25b" stroke-width="20" stroke-dasharray="330 160" transform="rotate(150 360 70)"/>
    <path d="M0 185 Q130 160 250 200 L260 345 L0 345Z" fill="url(#limeFade)"/>
    <path d="M0 342 Q130 310 250 318 Q380 322 470 395 L470 1176 L0 1176Z" fill="#1c2347"/>
    <path d="M0 385 Q70 330 150 318" fill="none" stroke="#dbe25b" stroke-width="9"/>
    <path d="M270 322 Q400 330 470 410" fill="none" stroke="#dbe25b" stroke-width="9"/>
    <path d="M25 430 Q70 375 130 360" fill="none" stroke="#dbe25b" stroke-width="4"/>
    <g stroke="#dbe25b" stroke-width="1.5">
      <line x1="70" y1="600" x2="70" y2="624"/>
      <line x1="181" y1="600" x2="181" y2="624"/>
      <line x1="291" y1="600" x2="291" y2="624"/>
      <line x1="402" y1="600" x2="402" y2="624"/>
    </g>
    <g stroke="#ffffff" stroke-opacity=".5" stroke-dasharray="3 3">
      <line x1="124" y1="660" x2="124" y2="755"/>
      <line x1="234" y1="660" x2="234" y2="755"/>
      <line x1="344" y1="660" x2="344" y2="755"/>
    </g>
    <path d="M0 905 C40 812 140 776 235 776 C330 776 430 812 470 905" fill="none" stroke="#ffffff" stroke-opacity=".6" stroke-dasharray="4 4"/>
    <path d="M0 925 C45 828 140 790 235 790 C330 790 425 828 470 925 L470 1176 L0 1176Z" fill="#dbe25b"/>
    <line x1="124" y1="972" x2="346" y2="972" stroke="#1c2347" stroke-opacity=".6" stroke-dasharray="4 3"/>
    <path d="M0 1176 L0 1124 Q0 1086 40 1086 L430 1086 Q470 1086 470 1124 L470 1176Z" fill="#1c2347"/>
  </svg>

  <div class="logo-tab"><span class="dot"></span><span class="name">Kalvento</span></div>

  <h1 class="headline"><span class="l1">Erfolg</span><span class="l2">Durch</span><span class="l3">Innovation</span></h1>

  <div class="brand"><span class="name">Kalvento</span><span class="tag">SIMULATION &amp; ANALYTICS</span></div>

  <h2 class="pill pill-about">About our service</h2>

  <div class="service-photo ph1" role="img" aria-label="Photo of hands on a laptop showing data charts"></div>
  <div class="service-photo ph2" role="img" aria-label="Photo of an engineer working in a simulation lab"></div>
  <div class="service-photo ph3" role="img" aria-label="Photo of a woman working at a computer"></div>
  <div class="service-photo ph4" role="img" aria-label="Photo of a hand pointing at a web application on a screen"></div>

  <div class="service-label lb1">Data Analysis</div>
  <div class="service-label lb2">Simulation</div>
  <div class="service-label lb3">Optimization</div>
  <div class="service-label lb4">Data Analysis</div>

  <p class="service-text tx1">Data analysis makes processes visible, identifies patterns, and creates an objective basis for decisions. We structure, clean, and analyze data so that it generates real value.</p>
  <p class="service-text tx2">Simulation digitally maps real processes so that workflows, capacities and variants can be tested without risk.</p>
  <p class="service-text tx3">Optimization automatically searches for the best solution be it in planning, resources, routes, or processes. Using algorithms and intelligent models, we find options that reduce</p>
  <p class="service-text tx4">We develop custom web applications that combine data, simulations, and optimizations in a user-friendly tool. This results in solutions that can be used directly in everyday life – simply, quickly, and without installation.</p>

  <h2 class="pill pill-grow">Grow your business</h2>
  <p class="grow-copy">Through simulation, data analysis and optimization, we develop solutions that make complex processes visible</p>

  <div class="call">
    <svg width="26" height="44" viewBox="0 0 26 44" aria-hidden="true"><path d="M20 2 C8 4 2 14 2 22 C2 30 8 40 20 42 L24 34 C18 33 14 28 14 22 C14 16 18 11 24 10Z" fill="#1c2347"/></svg>
    <div><span class="label">CALL FOR MORE INFO</span><span class="number">+41 81 555 04 38</span></div>
  </div>

  <div class="footer-info">
    <div class="info-item">
      <svg class="icon" viewBox="0 0 18 18" aria-hidden="true"><circle cx="9" cy="9" r="9" fill="#dbe25b"/><path d="M9 4a3.4 3.4 0 0 0-3.4 3.4C5.6 10 9 14 9 14s3.4-4 3.4-6.6A3.4 3.4 0 0 0 9 4z" fill="#1c2347"/><circle cx="9" cy="7.4" r="1.2" fill="#dbe25b"/></svg>
      <span>Talackerweg 9<br>7416 Rheinau</span>
    </div>
    <div class="info-item">
      <svg class="icon" viewBox="0 0 18 18" aria-hidden="true"><circle cx="9" cy="9" r="9" fill="#dbe25b"/><rect x="4.5" y="5.5" width="9" height="7" rx="1" fill="#1c2347"/><path d="M4.8 6l4.2 3.5L13.2 6" fill="none" stroke="#dbe25b" stroke-width="1"/></svg>
      <span><span class="small">Visit our email</span><span class="mail">info@kalvento.ch</span></span>
    </div>
    <div class="info-item">
      <svg class="icon" viewBox="0 0 18 18" aria-hidden="true"><circle cx="9" cy="9" r="9" fill="#dbe25b"/><path d="M9 4a3.4 3.4 0 0 0-3.4 3.4C5.6 10 9 14 9 14s3.4-4 3.4-6.6A3.4 3.4 0 0 0 9 4z" fill="#1c2347"/><circle cx="9" cy="7.4" r="1.2" fill="#dbe25b"/></svg>
      <span>Lindenhofstrasse 4,<br>8693 Seewiler</span>
    </div>
  </div>
</main>
</body>
</html>
```